WordPress Website for Accounting Firm

I have attached an excel sheet showing what i need done for my accounting website. Currently i have a WP website but its not live and do not like it. I can give a link if that will help. Total pages is around 12. I can buy and supply the images but have provided indication of what i want in the excel. I will need the designer to do the coding to make the website fully functional. I want a clean look and attractive. Don't want too dark colors. Once i like the landing page, i will need the designer to code code the website. Just want to look first. I will provide the logo file and put the contents myself. Just put dummy contents for now to show how it will look.
Updates
Can you please use the attached images so i can see how nit will look on the coverage as an option. These are from pixelharbor
264918053
418273596
1537206419
1096382147
Currently there are only 2 provided by myself as Photo 1 and Photo 2
Many Thanks!
Industry/Entity Type
Accounting and Finance
Number of Pages Required
5+ page

```html
<!DOCTYPE html>
<html lang="en">
<head>
<meta charset="utf-8">
<title>Ledgerline Advisory – Accountants &amp; Tax Advisors</title>
<link rel="stylesheet" href="https://fonts.googleapis.com/css2?family=Marcellus&family=Montserrat:wght@800&family=Nunito+Sans:wght@400;600;700&display=swap">
<style>
:root{
  --teal:#00a98a;
  --teal-dark:#008f75;
  --teal-light:#7fd9c6;
  --nav:#0f2a24;
  --ink:#1d1d1d;
  --text:#3a3a3a;
  --muted:#6a6a6a;
  --foot:#f3f8f8;
  --white:#ffffff;
}
*{margin:0;padding:0;box-sizing:border-box}
html,body{width:1200px;height:3193px;overflow:hidden;background:var(--white)}
body{position:relative;font-family:"Nunito Sans",Arial,sans-serif;color:var(--text)}
.abs{position:absolute}
.serif{font-family:"Marcellus",Georgia,serif;font-weight:400;color:var(--ink)}

/* header */
.topbar{left:0;top:0;width:1200px;height:65px;background:var(--teal)}
.brand{display:flex;align-items:center;gap:10px;color:var(--white)}
.brand-mark{width:52px;height:52px;border:3px solid currentColor;border-radius:50%}
.brand-name{font-size:13px;letter-spacing:.3px;line-height:1.2}
.brand-sub{font-size:7.5px;letter-spacing:2.6px;display:block}
.contact-item{display:flex;align-items:center;gap:9px;color:var(--white);font-size:11px;line-height:1.35}
.contact-item b{font-size:13px;font-weight:400}
.ci-icon{width:30px;height:30px;border:1.5px solid var(--white);border-radius:50%;display:flex;align-items:center;justify-content:center}
.partner-badge{width:76px;height:44px;border-radius:22px;background:rgba(255,255,255,.22);border:1.5px solid rgba(255,255,255,.6)}
.navbar{left:0;top:65px;width:1200px;height:34px;background:var(--nav)}
.nav a{position:absolute;font-size:12px;color:var(--white);text-decoration:none;letter-spacing:.3px}
.nav a.active{color:var(--teal)}
.social-dot{width:20px;height:20px;border-radius:50%;background:var(--white)}

/* hero */
.hero{left:0;top:99px;width:1200px;height:470px;overflow:hidden}
.hero-bg{left:0;top:0;width:1200px;height:470px;background:linear-gradient(100deg,#f4f5f6 0%,#e9ecee 45%,#dfe4e6 100%)}
.hero-kicker{left:130px;top:132px;font-size:21px;color:var(--ink)}
.hero-title{left:130px;top:154px;font-size:46px;letter-spacing:.5px}
.hero-text{left:130px;top:218px;width:320px;font-size:13px;line-height:1.55;color:var(--text)}
.btn{display:flex;align-items:center;background:var(--teal);color:var(--white);font-size:12px;font-weight:600;letter-spacing:.5px;text-decoration:none}
.btn span{flex:1;text-align:center;padding-right:18px}
.btn i{width:28px;height:28px;border-radius:50%;background:var(--white);margin-right:-14px;display:flex;align-items:center;justify-content:center}
.arrow-lg{width:40px;height:70px}

/* about */
.about-title{left:690px;top:672px;font-size:38px}
.about-text{left:690px;top:743px;width:385px;font-size:13px;line-height:20px;color:var(--text)}

/* why */
.why-title{left:0;top:1170px;width:1200px;text-align:center;font-size:38px}
.check-row{display:flex;align-items:center;gap:10px;width:430px;font-size:13px;line-height:17px;color:var(--ink)}
.check-row.right{width:400px}
.tick{flex:none;width:32px;height:32px}
.divider{left:600px;top:1258px;width:1px;height:263px;background:#5b6b68}

/* testimonials */
.photo-area{background:radial-gradient(ellipse at 55% 45%,#e9c2ab 0%,#f3dccd 40%,rgba(255,255,255,0) 72%)}
.quote-head{left:0;top:1700px;width:1200px;text-align:center;font-family:"Montserrat",Arial,sans-serif;font-weight:800;font-size:82px;line-height:76px;letter-spacing:-2px;color:#262626}
.quote-head .accent{color:var(--teal)}
.card{top:1974px;width:300px;height:202px;border:1.5px solid var(--teal);border-bottom-left-radius:40px;background:var(--white);padding:16px 22px 0 18px;font-size:12px;line-height:19px;color:var(--muted)}
.card.featured{background:var(--teal);color:#e9fffa}
.person{position:absolute;left:18px;top:128px;display:flex;align-items:center;gap:10px}
.avatar{width:54px;height:54px;border-radius:50%;background:linear-gradient(135deg,#c9d2d0,#8f9a98)}
.person b{display:block;font-size:14px;font-weight:400;color:var(--ink)}
.person small{font-size:10px;color:var(--muted)}
.featured .person b,.featured .person small{color:var(--white)}
.qmark{position:absolute;right:14px;bottom:12px;font-family:Georgia,serif;font-size:54px;line-height:30px;color:#555}
.featured .qmark{color:var(--teal-light)}
.round-btn{width:36px;height:36px;border-radius:50%;border:1px solid #bfc7c5;background:var(--white);display:flex;align-items:center;justify-content:center}

/* industries */
.ind-bg{left:0;top:2244px;width:1200px;height:540px;background:linear-gradient(180deg,#ffffff 0%,#eef6f4 25%,#f1f7f6 80%,#ffffff 100%)}
.ind-title{left:0;top:2350px;width:1200px;text-align:center;font-size:38px}
.industry{display:flex;align-items:center;gap:10px;font-size:14px;font-weight:600;color:var(--ink)}
.ind-icon{width:48px;height:48px;flex:none}

/* footer */
.footer-bg{left:0;top:2770px;width:1200px;height:423px;background:var(--foot)}
.foot-h{font-size:18px;color:var(--ink);font-weight:600}
.foot-links{list-style:none;font-size:11.5px;color:var(--ink)}
.foot-links li{height:29.5px}
.foot-links li::before{content:"» ";color:var(--teal)}
.foot-contact{display:flex;align-items:center;gap:10px;font-size:11.5px;line-height:15px;color:var(--ink)}
.fc-icon{width:30px;height:30px;flex:none;border:1.5px solid #9aa8a5;border-radius:50%;display:flex;align-items:center;justify-content:center}
.newsletter{display:flex;width:240px;height:32px}
.newsletter .field{flex:1;background:#111;color:#ddd;font-size:9px;padding:11px 10px}
.newsletter .send{width:66px;background:var(--teal);color:var(--white);font-size:10px;font-weight:700;text-align:center;padding-top:10px}
.foot-social{width:32px;height:32px;border-radius:50%;border:2px solid var(--teal);background:var(--white)}
.rule{left:130px;top:3085px;width:940px;height:1px;background:#dde5e3}
.copyright{left:0;top:3128px;width:1200px;text-align:center;font-size:10px;color:#555}
.copyright span{color:var(--teal)}
</style>
</head>
<body>

<!-- header -->
<div class="abs topbar"></div>
<div class="abs brand" style="left:130px;top:4px">
  <div class="brand-mark"></div>
  <div class="brand-name">LEDGERLINE | ADVISORY<span class="brand-sub">ACCOUNTANTS • TAX ADVISORS</span></div>
</div>
<div class="abs contact-item" style="left:589px;top:17px">
  <div class="ci-icon"><svg width="14" height="14" viewBox="0 0 24 24"><path d="M6.6 10.8a15 15 0 006.6 6.6l2.2-2.2a1 1 0 011-.25 11.4 11.4 0 003.6.57 1 1 0 011 1V20a1 1 0 01-1 1A17 17 0 013 4a1 1 0 011-1h3.5a1 1 0 011 1c0 1.25.2 2.45.57 3.57a1 1 0 01-.25 1z" fill="#fff"/></svg></div>
  <div>Call Us:<br><b>+2 (555) 246 7310</b></div>
</div>
<div class="abs contact-item" style="left:771px;top:17px">
  <div class="ci-icon"><svg width="14" height="14" viewBox="0 0 24 24"><rect x="3" y="6" width="18" height="12" rx="1.5" fill="none" stroke="#fff" stroke-width="2"/><path d="M3 7l9 6 9-6" fill="none" stroke="#fff" stroke-width="2"/></svg></div>
  <div>Mail Us:<br><b>info@ledgerlineadvisory.com</b></div>
</div>
<div class="abs partner-badge" style="left:992px;top:10px" role="img" aria-label="Partner software badges"></div>

<div class="abs navbar"></div>
<nav class="nav">
  <a class="active" style="left:505px;top:76px">HOME</a>
  <a style="left:584px;top:76px">SOLUTION</a>
  <a style="left:687px;top:76px">CLIENTS</a>
  <a style="left:777px;top:76px">CONTACT US</a>
  <a style="left:895px;top:76px">CLIENT RESOURCES</a>
</nav>
<div class="abs social-dot" style="left:1050px;top:73px"></div>

<!-- hero -->
<section class="abs hero">
  <div class="abs hero-bg" role="img" aria-label="Blurred office background with monitors and charts"></div>
  <svg class="abs" style="left:0;top:0" width="1200" height="470" viewBox="0 0 1200 470">
    <defs>
      <linearGradient id="heroPhoto" x1="0" y1="0" x2="1" y2="1">
        <stop offset="0" stop-color="#0c8f76"/><stop offset=".55" stop-color="#00a98a"/><stop offset="1" stop-color="#0b6f5c"/>
      </linearGradient>
    </defs>
    <circle cx="740" cy="225" r="222" fill="url(#heroPhoto)" role="img" aria-label="Photo of a smiling accountant in glasses and tie"/>
    <path d="M0 370 Q600 470 1200 370 L1200 470 L0 470Z" fill="#fff"/>
    <path d="M0 370 Q600 470 1200 370" fill="none" stroke="var(--teal)" stroke-width="5"/>
  </svg>
  <div class="abs hero-kicker serif">Trusted Accountants &amp;</div>
  <div class="abs hero-title serif">Business Advisor</div>
  <p class="abs hero-text">Sed ut perspiciatis unde omnis iste natus error sit voluptatem accusantium doloremque...</p>
  <a class="abs btn" style="left:130px;top:279px;width:144px;height:47px"><span>CONTACT US</span><i><svg width="12" height="8" viewBox="0 0 12 8"><path d="M0 4h10M7 1l3 3-3 3" fill="none" stroke="#333" stroke-width="1"/></svg></i></a>
  <svg class="abs arrow-lg" style="left:46px;top:192px" viewBox="0 0 40 70"><path d="M36 2L4 35l32 33" fill="none" stroke="#111" stroke-width="2.5"/></svg>
  <svg class="abs arrow-lg" style="left:1116px;top:192px" viewBox="0 0 40 70"><path d="M4 2l32 33L4 68" fill="none" stroke="#111" stroke-width="2.5"/></svg>
</section>

<!-- about -->
<svg class="abs" style="left:130px;top:618px" width="455" height="415" viewBox="0 0 455 415" role="img" aria-label="Photo of a smiling businesswoman at her desk, with a small photo of hands typing">
  <defs>
    <linearGradient id="aboutPhoto" x1="0" y1="0" x2="1" y2="1">
      <stop offset="0" stop-color="#bfe6dc"/><stop offset=".6" stop-color="#d9ece6"/><stop offset="1" stop-color="#9fc9be"/>
    </linearGradient>
  </defs>
  <circle cx="80" cy="97" r="34" fill="#b7ddd3"/>
  <path d="M195 10c40-30 110 20 135 90 25 70 10 170-40 230-40 50-120 90-190 80C40 400 0 350 5 290c5-50 60-80 90-120 30-40 50-110 100-160z" fill="url(#aboutPhoto)"/>
  <circle cx="392" cy="347" r="59" fill="#c4d6d3"/>
</svg>
<h2 class="abs about-title serif">About Us</h2>
<p class="abs about-text">Sed ut perspiciatis unde omnis iste natus error sit voluptatem accusantium doloremque laudantium, totam rem aperiam, eaque ipsa quae ab illo inventore veritatis et quasi architecto beatae vitae dicta sunt explicabo. Nemo enim ipsam voluptatem quia voluptas sit aspernatur aut odit aut fugit, sed quia consequuntur magni dolores eos qui ratione voluptatem sequi nesciunt.</p>
<a class="abs btn" style="left:690px;top:921px;width:143px;height:47px"><span>READ MORE</span><i><svg width="12" height="8" viewBox="0 0 12 8"><path d="M0 4h10M7 1l3 3-3 3" fill="none" stroke="#333" stroke-width="1"/></svg></i></a>

<!-- why choose us -->
<svg class="abs" style="left:0;top:1085px" width="1200" height="540" viewBox="0 0 1200 540">
  <defs>
    <linearGradient id="mintBand" x1="0" y1="0" x2="1" y2="1">
      <stop offset="0" stop-color="#e8f7f3"/><stop offset=".5" stop-color="#f2faf8"/><stop offset="1" stop-color="#d6f1ea"/>
    </linearGradient>
  </defs>
  <path d="M0 0 Q600 120 1200 0 L1200 500 Q600 460 0 535Z" fill="url(#mintBand)"/>
</svg>
<h2 class="abs why-title serif">Why Choose Us</h2>
<svg width="0" height="0" style="position:absolute">
  <symbol id="tick" viewBox="0 0 32 32"><circle cx="16" cy="16" r="15" fill="var(--teal)" stroke="#bfe9df" stroke-width="2"/><path d="M10 16.5l4.2 4.2L22.5 11" fill="none" stroke="#fff" stroke-width="2.2"/></symbol>
</svg>
<div class="abs check-row" style="left:130px;top:1260px"><svg class="tick"><use href="#tick"/></svg>We specialise in accounting and tax solutions for all business structures and industries</div>
<div class="abs check-row" style="left:130px;top:1320px"><svg class="tick"><use href="#tick"/></svg>Our team are qualified professionals with 50+ years of combined experience in CA industry</div>
<div class="abs check-row" style="left:130px;top:1371px"><svg class="tick"><use href="#tick"/></svg>We are Accessable 7 days a week</div>
<div class="abs check-row" style="left:130px;top:1427px"><svg class="tick"><use href="#tick"/></svg>We constantly upskill to keep up with changes to tax laws and legislation</div>
<div class="abs check-row" style="left:130px;top:1477px"><svg class="tick"><use href="#tick"/></svg>Our advise is explained in plain english so you understand</div>
<div class="abs divider"></div>
<div class="abs check-row right" style="left:683px;top:1262px"><svg class="tick"><use href="#tick"/></svg>Our fees are not only fair but very competitive</div>
<div class="abs check-row right" style="left:683px;top:1320px"><svg class="tick"><use href="#tick"/></svg>We don't believe in one size fits all, we listen to client's challenges indiviually</div>
<div class="abs check-row right" style="left:683px;top:1371px"><svg class="tick"><use href="#tick"/></svg>Our level of service and work ethics is no different to any other large CA practices</div>
<div class="abs check-row right" style="left:683px;top:1425px"><svg class="tick"><use href="#tick"/></svg>We have affiliations with other business partners</div>
<div class="abs check-row right" style="left:683px;top:1477px"><svg class="tick"><use href="#tick"/></svg>We keep up with everchanging cloud based technology</div>

<!-- testimonials -->
<div class="abs photo-area" style="left:70px;top:1590px;width:320px;height:360px" role="img" aria-label="Photo of a hand making an OK gesture"></div>
<div class="abs photo-area" style="left:820px;top:1640px;width:320px;height:335px" role="img" aria-label="Photo of a hand making an OK gesture"></div>
<h2 class="abs quote-head">Don’t take<br><span class="accent">our word</span><br>for it</h2>

<div class="abs round-btn" style="left:47px;top:2056px"><svg width="8" height="12" viewBox="0 0 8 12"><path d="M6 1L1 6l5 5" fill="none" stroke="#333" stroke-width="1.5"/></svg></div>
<div class="abs round-btn" style="left:1116px;top:2056px"><svg width="8" height="12" viewBox="0 0 8 12"><path d="M2 1l5 5-5 5" fill="none" stroke="#333" stroke-width="1.5"/></svg></div>

<article class="abs card" style="left:130px">
  Sed ut perspiciatis unde omnis iste natus error sit voluptatem accusantium doloremque laudantium, totam rem aperiam, eaque ipsa quae ab illo inventore veritatis et quasi architecto beatae...
  <div class="person"><div class="avatar" role="img" aria-label="Client portrait"></div><div><b>Marcus Delane</b><small>Advisor</small></div></div>
  <div class="qmark">”</div>
</article>
<article class="abs card featured" style="left:450px">
  Sed ut perspiciatis unde omnis iste natus error sit voluptatem accusantium doloremque laudantium, totam rem aperiam, eaque ipsa quae ab illo inventore veritatis et quasi architecto beatae...
  <div class="person"><div class="avatar" role="img" aria-label="Client portrait"></div><div><b>Oren Castell</b><small>Accountant</small></div></div>
  <div class="qmark">”</div>
</article>
<article class="abs card" style="left:770px">
  Sed ut perspiciatis unde omnis iste natus error sit voluptatem accusantium doloremque laudantium, totam rem aperiam, eaque ipsa quae ab illo inventore veritatis et quasi architecto beatae...
  <div class="person"><div class="avatar" role="img" aria-label="Client portrait"></div><div><b>Lena Harwick</b><small>Accontacnt</small></div></div>
  <div class="qmark">”</div>
</article>

<!-- industries -->
<div class="abs ind-bg"></div>
<h2 class="abs ind-title serif">Industries We Represent</h2>
<svg width="0" height="0" style="position:absolute">
  <symbol id="ind" viewBox="0 0 48 48"><circle cx="24" cy="24" r="22.5" fill="#fff" stroke="var(--teal)" stroke-width="2"/><circle cx="24" cy="24" r="17" fill="none" stroke="#bfe9df" stroke-width="1"/><rect x="16" y="15" width="16" height="18" rx="2" fill="none" stroke="var(--teal)" stroke-width="2"/><path d="M20 21h8M20 25h8M20 29h5" stroke="var(--teal)" stroke-width="1.5"/></symbol>
</svg>
<div class="abs industry" style="left:130px;top:2451px"><svg class="ind-icon"><use href="#ind"/></svg>Healthcare Specialists</div>
<div class="abs industry" style="left:383px;top:2451px"><svg class="ind-icon"><use href="#ind"/></svg>Construction</div>
<div class="abs industry" style="left:629px;top:2451px"><svg class="ind-icon"><use href="#ind"/></svg>Professional Services</div>
<div class="abs industry" style="left:877px;top:2451px"><svg class="ind-icon"><use href="#ind"/></svg>Legal</div>
<div class="abs industry" style="left:130px;top:2514px"><svg class="ind-icon"><use href="#ind"/></svg>Contractors</div>
<div class="abs industry" style="left:383px;top:2514px"><svg class="ind-icon"><use href="#ind"/></svg>Architecture</div>
<div class="abs industry" style="left:629px;top:2514px"><svg class="ind-icon"><use href="#ind"/></svg>Retail</div>
<div class="abs industry" style="left:877px;top:2514px"><svg class="ind-icon"><use href="#ind"/></svg>Medical Practiniors</div>
<div class="abs industry" style="left:130px;top:2578px"><svg class="ind-icon"><use href="#ind"/></svg>Manufacturing</div>
<div class="abs industry" style="left:383px;top:2578px"><svg class="ind-icon"><use href="#ind"/></svg>Real Estate Rentals</div>
<div class="abs industry" style="left:629px;top:2578px"><svg class="ind-icon"><use href="#ind"/></svg>Childcare</div>
<div class="abs industry" style="left:877px;top:2578px"><svg class="ind-icon"><use href="#ind"/></svg>Film Industry</div>

<!-- footer -->
<div class="abs footer-bg"></div>
<svg class="abs" style="left:0;top:2740px" width="1200" height="70" viewBox="0 0 1200 70">
  <path d="M0 10 Q600 110 1200 10 L1200 0 L0 0Z" fill="#f1f7f6"/>
  <path d="M0 10 Q600 110 1200 10" fill="none" stroke="var(--teal)" stroke-width="6"/>
</svg>
<div class="abs brand" style="left:130px;top:2846px;color:var(--ink)">
  <div class="brand-mark" style="border-color:var(--ink)"></div>
  <div class="brand-name">LEDGERLINE | ADVISORY<span class="brand-sub">ACCOUNTANTS • TAX ADVISORS</span></div>
</div>
<div class="abs" style="left:130px;top:2950px;font-size:14px;color:var(--ink)">Newsletter</div>
<div class="abs newsletter" style="left:130px;top:2977px"><div class="field">Enter Your Email:</div><div class="send">Subscribe</div></div>
<div class="abs foot-social" style="left:130px;top:3029px"></div>

<div class="abs foot-h" style="left:449px;top:2843px">Quick Links</div>
<ul class="abs foot-links" style="left:449px;top:2887px">
  <li>Home</li><li>Our Solutions</li><li>Clients</li><li>Contact Us</li><li>Clients Resources</li>
</ul>
<div class="abs foot-h" style="left:670px;top:2843px">Solution</div>
<ul class="abs foot-links" style="left:670px;top:2887px">
  <li>Tax and Accounting</li><li>Specialist</li><li>Cloud Accounting</li>
</ul>
<div class="abs foot-h" style="left:891px;top:2843px">Contact Us</div>
<div class="abs foot-contact" style="left:891px;top:2885px"><div class="fc-icon"><svg width="12" height="14" viewBox="0 0 12 16"><path d="M6 15S1 9 1 6a5 5 0 0110 0c0 3-5 9-5 9z" fill="none" stroke="var(--teal)" stroke-width="1.6"/><circle cx="6" cy="6" r="1.8" fill="var(--teal)"/></svg></div>P O Box 50721, Greenfield,<br>Harbourton 4187</div>
<div class="abs foot-contact" style="left:891px;top:2925px"><div class="fc-icon"><svg width="13" height="13" viewBox="0 0 24 24"><path d="M6.6 10.8a15 15 0 006.6 6.6l2.2-2.2a1 1 0 011-.25 11.4 11.4 0 003.6.57 1 1 0 011 1V20a1 1 0 01-1 1A17 17 0 013 4a1 1 0 011-1h3.5a1 1 0 011 1c0 1.25.2 2.45.57 3.57a1 1 0 01-.25 1z" fill="var(--teal)"/></svg></div>021 587 406</div>
<div class="abs foot-contact" style="left:891px;top:2966px"><div class="fc-icon"><svg width="13" height="13" viewBox="0 0 24 24"><rect x="3" y="6" width="18" height="12" rx="1.5" fill="none" stroke="var(--teal)" stroke-width="2"/><path d="M3 7l9 6 9-6" fill="none" stroke="var(--teal)" stroke-width="2"/></svg></div>info@ledgerline.co.nz</div>
<div class="abs foot-contact" style="left:891px;top:3008px"><div class="fc-icon"><svg width="13" height="13" viewBox="0 0 24 24"><rect x="3" y="6" width="18" height="12" rx="1.5" fill="none" stroke="var(--teal)" stroke-width="2"/><path d="M3 7l9 6 9-6" fill="none" stroke="var(--teal)" stroke-width="2"/></svg></div>office@ledgerline.co.nz</div>

<div class="abs rule"></div>
<p class="abs copyright">Copyright © 2022 <span>Ledgerline Advisory</span>. All Rights Reserved.</p>

</body>
</html>
```